New italian pizza restaurant in Australia, looking for a clean and crisp new take away leaflet de...

We require a leaflet for a take away menu / introduction to the area for our new italian pizza restaurant. AS we are a brand new business we need to get the word out about opening and specials as well as a takeaway menu. I have attached logo and menu items along with a basic design concept to help speed up the process.

Target Market(s)

Widest age range possible, families

Colors

Designer to choose colors to be used in the design.

```html
<!DOCTYPE html>
<html lang="en">
<head>
<meta charset="utf-8">
<title>Corvello Pizzeria – Takeaway Menu</title>
<link rel="stylesheet" href="https://fonts.googleapis.com/css2?family=Rubik:wght@700&family=Fjalla+One&family=Arimo:wght@400&family=Oswald:wght@500&display=swap">
<style>
:root{
  --ink:#0c0c0c;
  --panel:#111312;
  --green:#3a9150;
  --green-dark:#2c7440;
  --green-text:#4fae66;
  --red:#e0401f;
  --white:#f4f4f4;
  --muted:#d8d8d8;
  --bg:#e9eaea;
}
*{box-sizing:border-box;margin:0;padding:0}
html,body{width:1200px;height:1200px;overflow:hidden;background:var(--bg)}
body{display:flex;flex-direction:column;align-items:center;justify-content:center;gap:26px;font-family:"Arimo",Arial,sans-serif;color:var(--white)}
.spread{width:734px;height:570px;background:var(--ink);display:flex;flex-direction:column;box-shadow:0 3px 10px rgba(0,0,0,.25)}
.band{height:22px;background:var(--green);flex:none;position:relative}
.band.top{border-bottom:3px solid var(--red)}
.band.bottom{border-top:3px solid var(--red)}
.panels{flex:1;display:flex;min-height:0}
.panel{padding:24px 14px 10px;display:flex;flex-direction:column;border-right:2px solid var(--green-dark)}
.panel:last-child{border-right:none}
.ribbon{align-self:center;font-family:"Rubik",Arial,sans-serif;font-weight:700;font-size:16px;color:var(--white);background:var(--green);padding:5px 34px;margin-bottom:8px;clip-path:polygon(0 0,100% 0,94% 50%,100% 100%,0 100%,6% 50%);transform:rotate(-1.5deg)}
.note{text-align:center;font-size:7.5px;color:var(--white);margin:-2px 0 8px}
.sizes{display:flex;justify-content:flex-end;gap:8px;font-family:"Fjalla One",sans-serif;font-size:6.5px;color:var(--green-text);margin-bottom:6px}
.sizes span{width:21px;text-align:center}
.sizes .lbl{width:auto;color:#8a8a8a}
.item{display:flex;align-items:flex-start;gap:6px;margin-bottom:12px}
.item .icon{flex:none;width:18px;height:18px}
.item .text{flex:1;min-width:0}
.name{font-family:"Fjalla One",sans-serif;font-size:7.5px;color:var(--green-text);text-transform:uppercase;display:flex;align-items:center;gap:3px}
.name::after{content:"";flex:1;border-bottom:1px dashed #555}
.desc{font-size:6.5px;line-height:1.2;color:var(--muted)}
.prices{display:flex;gap:5px;flex:none}
.p{display:inline-block;min-width:21px;height:17px;line-height:17px;text-align:center;background:var(--green);color:var(--white);font-family:"Fjalla One",sans-serif;font-size:7.5px;font-weight:400;border-radius:2px;padding:0 2px}
.p sup{font-size:5px}
.cols{display:flex;gap:18px}
.cols>div{flex:1}
.num{fill:none;stroke:var(--white);stroke-width:1.2}
.num-text{font-family:"Fjalla One",sans-serif;font-size:7px;fill:var(--green-text)}
.sub{text-align:center;font-size:7.5px;margin-bottom:10px}
.simple .item{margin-bottom:9px}
.kids{display:flex;align-items:center;gap:10px;justify-content:center;margin-bottom:10px}
.kids .price{font-family:"Fjalla One",sans-serif;font-size:13px}
.kids ul{list-style:none;font-family:"Fjalla One",sans-serif;font-size:6.5px;color:var(--green-text);line-height:1.45}
.cover{flex:1;padding:0;position:relative;display:flex;flex-direction:column}
.cover-art{height:190px;background:radial-gradient(circle at 60% 40%,#2a3a2e,#141816 75%)}
.brand{display:flex;flex-direction:column;align-items:center;gap:8px;margin-top:30px}
.brand .dot{width:14px;height:14px;border-radius:50%;background:var(--red)}
.brand-name{font-family:"Oswald",sans-serif;font-weight:500;font-size:22px;color:var(--white);letter-spacing:1px;text-align:center;line-height:1.25}
.contact{text-align:center;font-size:10px;line-height:1.6;margin-top:auto;margin-bottom:40px}
</style>
</head>
<body>

<!-- Inside spread -->
<section class="spread inside">
  <div class="band top"></div>
  <div class="panels">
    <div class="panel pizza" style="flex:2">
      <div class="cols">
        <div>
          <h2 class="ribbon" style="margin-bottom:12px">Pizza</h2>
          <div class="sizes"><span class="lbl">size</span><span>Small</span><span>Large</span><span>Family</span></div>
          <div class="item"><svg class="icon" viewBox="0 0 18 18"><path class="num" d="M2 3h14L9 17z"/><text class="num-text" x="5" y="11">01</text></svg><div class="text"><div class="name">Capricciosa</div><div class="desc">tomato, cheese, ham, mushrooms, olives</div></div><div class="prices"><b class="p"><sup>$</sup>9</b><b class="p"><sup>$</sup>15</b><b class="p"><sup>$</sup>18</b></div></div>
          <div class="item"><svg class="icon" viewBox="0 0 18 18"><path class="num" d="M2 3h14L9 17z"/><text class="num-text" x="5" y="11">02</text></svg><div class="text"><div class="name">Napoli</div><div class="desc">tomato, cheese, olives, anchovies</div></div><div class="prices"><b class="p"><sup>$</sup>9</b><b class="p"><sup>$</sup>15</b><b class="p"><sup>$</sup>18</b></div></div>
          <div class="item"><svg class="icon" viewBox="0 0 18 18"><path class="num" d="M2 3h14L9 17z"/><text class="num-text" x="5" y="11">03</text></svg><div class="text"><div class="name">American</div><div class="desc">tomato, cheese, salami</div></div><div class="prices"><b class="p"><sup>$</sup>9</b><b class="p"><sup>$</sup>15</b><b class="p"><sup>$</sup>18</b></div></div>
          <div class="item"><svg class="icon" viewBox="0 0 18 18"><path class="num" d="M2 3h14L9 17z"/><text class="num-text" x="5" y="11">04</text></svg><div class="text"><div class="name">Vegetarian</div><div class="desc">tomato, cheese, mushroom, onions, capsicum, olives</div></div><div class="prices"><b class="p"><sup>$</sup>9</b><b class="p"><sup>$</sup>15</b><b class="p"><sup>$</sup>18</b></div></div>
          <div class="item"><svg class="icon" viewBox="0 0 18 18"><path class="num" d="M2 3h14L9 17z"/><text class="num-text" x="5" y="11">05</text></svg><div class="text"><div class="name">Seafood</div><div class="desc">tomato, cheese, prawns, clams, anchovies</div></div><div class="prices"><b class="p"><sup>$</sup>9.5</b><b class="p"><sup>$</sup>15.5</b><b class="p"><sup>$</sup>19</b></div></div>
          <div class="item"><svg class="icon" viewBox="0 0 18 18"><path class="num" d="M2 3h14L9 17z"/><text class="num-text" x="5" y="11">06</text></svg><div class="text"><div class="name">The Hot One</div><div class="desc">tomato, cheese, ham, salami, chilli</div></div><div class="prices"><b class="p"><sup>$</sup>9</b><b class="p"><sup>$</sup>15</b><b class="p"><sup>$</sup>18</b></div></div>
          <div class="item"><svg class="icon" viewBox="0 0 18 18"><path class="num" d="M2 3h14L9 17z"/><text class="num-text" x="5" y="11">07</text></svg><div class="text"><div class="name">Margherita</div><div class="desc">tomato, cheese, oregano</div></div><div class="prices"><b class="p"><sup>$</sup>8.5</b><b class="p"><sup>$</sup>14.5</b><b class="p"><sup>$</sup>17</b></div></div>
          <div class="item"><svg class="icon" viewBox="0 0 18 18"><path class="num" d="M2 3h14L9 17z"/><text class="num-text" x="5" y="11">08</text></svg><div class="text"><div class="name">The Lot</div><div class="desc">tomato, cheese, ham, salami, bacon, mushroom, onions, capsicum, pineapple, olives</div></div><div class="prices"><b class="p"><sup>$</sup>10</b><b class="p"><sup>$</sup>16</b><b class="p"><sup>$</sup>19</b></div></div>
          <div class="item"><svg class="icon" viewBox="0 0 18 18"><path class="num" d="M2 3h14L9 17z"/><text class="num-text" x="5" y="11">09</text></svg><div class="text"><div class="name">Mexican</div><div class="desc">tomato, cheese, salami, capsicum, chilli</div></div><div class="prices"><b class="p"><sup>$</sup>9</b><b class="p"><sup>$</sup>15</b><b class="p"><sup>$</sup>18</b></div></div>
        </div>
        <div>
          <div class="sizes" style="margin-top:20px"><span class="lbl">size</span><span>Small</span><span>Large</span><span>Family</span></div>
          <div class="item"><svg class="icon" viewBox="0 0 18 18"><path class="num" d="M2 3h14L9 17z"/><text class="num-text" x="5" y="11">10</text></svg><div class="text"><div class="name">Chicken</div><div class="desc">tomato, cheese, chicken, BBQ sauce</div></div><div class="prices"><b class="p"><sup>$</sup>9</b><b class="p"><sup>$</sup>15</b><b class="p"><sup>$</sup>18</b></div></div>
          <div class="item"><svg class="icon" viewBox="0 0 18 18"><path class="num" d="M2 3h14L9 17z"/><text class="num-text" x="5" y="11">11</text></svg><div class="text"><div class="name">Meat Lovers</div><div class="desc">tomato, cheese, ham, salami, bacon, BBQ sauce</div></div><div class="prices"><b class="p"><sup>$</sup>10</b><b class="p"><sup>$</sup>16</b><b class="p"><sup>$</sup>19</b></div></div>
          <div class="item"><svg class="icon" viewBox="0 0 18 18"><path class="num" d="M2 3h14L9 17z"/><text class="num-text" x="5" y="11">12</text></svg><div class="text"><div class="name">The House Pizza</div><div class="desc">tomato, cheese, ham, mushroom, capsicum</div></div><div class="prices"><b class="p"><sup>$</sup>9</b><b class="p"><sup>$</sup>15</b><b class="p"><sup>$</sup>18</b></div></div>
          <div class="item"><svg class="icon" viewBox="0 0 18 18"><path class="num" d="M2 3h14L9 17z"/><text class="num-text" x="5" y="11">13</text></svg><div class="text"><div class="name">Ceaser's Pizza</div><div class="desc">tomato, cheese, ham, mushroom, pineapple, prawns</div></div><div class="prices"><b class="p"><sup>$</sup>10</b><b class="p"><sup>$</sup>16</b><b class="p"><sup>$</sup>19</b></div></div>
          <div class="item"><svg class="icon" viewBox="0 0 18 18"><path class="num" d="M2 3h14L9 17z"/><text class="num-text" x="5" y="11">14</text></svg><div class="text"><div class="name">The Breakie Pizza</div><div class="desc">tomato, cheese, bacon, egg</div></div><div class="prices"><b class="p"><sup>$</sup>9</b><b class="p"><sup>$</sup>15</b><b class="p"><sup>$</sup>18</b></div></div>
          <div class="item"><svg class="icon" viewBox="0 0 18 18"><path class="num" d="M2 3h14L9 17z"/><text class="num-text" x="5" y="11">15</text></svg><div class="text"><div class="name">The Footy Special</div><div class="desc">tomato, cheese, ham, capsicum, onions, pineapple</div></div><div class="prices"><b class="p"><sup>$</sup>9</b><b class="p"><sup>$</sup>15</b><b class="p"><sup>$</sup>18</b></div></div>
          <div class="item"><svg class="icon" viewBox="0 0 18 18"><path class="num" d="M2 3h14L9 17z"/><text class="num-text" x="5" y="11">16</text></svg><div class="text"><div class="name">The Corvello</div><div class="desc">tomato, cheese ham, mushrooms, onions, olives</div></div><div class="prices"><b class="p"><sup>$</sup>9</b><b class="p"><sup>$</sup>15</b><b class="p"><sup>$</sup>18</b></div></div>
          <div class="item"><svg class="icon" viewBox="0 0 18 18"><path class="num" d="M2 3h14L9 17z"/><text class="num-text" x="5" y="11">17</text></svg><div class="text"><div class="name">The Corvo Special</div><div class="desc">tomato, cheese, ham, onions, bacon, egg</div></div><div class="prices"><b class="p"><sup>$</sup>10</b><b class="p"><sup>$</sup>16</b><b class="p"><sup>$</sup>19</b></div></div>
          <div class="item"><svg class="icon" viewBox="0 0 18 18"><path class="num" d="M2 3h14L9 17z"/><text class="num-text" x="5" y="11">18</text></svg><div class="text"><div class="name">Ham</div><div class="desc">tomato, cheese, ham</div></div><div class="prices"><b class="p"><sup>$</sup>8.5</b><b class="p"><sup>$</sup>14.5</b><b class="p"><sup>$</sup>17</b></div></div>
          <div class="item"><svg class="icon" viewBox="0 0 18 18"><path class="num" d="M2 3h14L9 17z"/><text class="num-text" x="5" y="11">19</text></svg><div class="text"><div class="name">Garlic</div><div class="desc">garlic, cheese, oregano</div></div><div class="prices"><b class="p"><sup>$</sup>8.5</b><b class="p"><sup>$</sup>14.5</b><b class="p"><sup>$</sup>17</b></div></div>
        </div>
      </div>
    </div>

    <div class="panel mains" style="flex:1">
      <h2 class="ribbon">Main Meals</h2>
      <p class="note">( all mains served with chips or salad )</p>
      <div class="item"><svg class="icon" viewBox="0 0 18 18"><circle class="num" cx="9" cy="9" r="7.5"/><text class="num-text" x="5" y="11.5">01</text></svg><div class="text"><div class="name">Scotch Fillet Steak 300g</div><div class="desc">grass fed, with your choice of Mushroom, Pepper or Garlic sauce</div></div><div class="prices"><b class="p"><sup>$</sup>25</b></div></div>
      <div class="item"><svg class="icon" viewBox="0 0 18 18"><circle class="num" cx="9" cy="9" r="7.5"/><text class="num-text" x="5" y="11.5">02</text></svg><div class="text"><div class="name">Calamari</div><div class="desc">Flash fried or crumbed squid with aioli</div></div><div class="prices"><b class="p"><sup>$</sup>19.5</b></div></div>
      <div class="item"><svg class="icon" viewBox="0 0 18 18"><circle class="num" cx="9" cy="9" r="7.5"/><text class="num-text" x="5" y="11.5">03</text></svg><div class="text"><div class="name">Chicken Parmigiana</div><div class="desc">Schnitzel topped with ham, Napoli sauce &amp; mozzarella</div></div><div class="prices"><b class="p"><sup>$</sup>19.5</b></div></div>
      <div class="item"><svg class="icon" viewBox="0 0 18 18"><circle class="num" cx="9" cy="9" r="7.5"/><text class="num-text" x="5" y="11.5">04</text></svg><div class="text"><div class="name">Veal Scallopini</div><div class="desc">with your choice of mushroom or creamy avocado sauce</div></div><div class="prices"><b class="p"><sup>$</sup>19.5</b></div></div>
      <div class="item"><svg class="icon" viewBox="0 0 18 18"><circle class="num" cx="9" cy="9" r="7.5"/><text class="num-text" x="5" y="11.5">05</text></svg><div class="text"><div class="name">Veal Parmigiana</div><div class="desc">schnitzel topped ham, Napoli sauce &amp; mozzarella</div></div><div class="prices"><b class="p"><sup>$</sup>19.5</b></div></div>
      <h2 class="ribbon" style="margin-top:14px">Salads</h2>
      <div class="item"><svg class="icon" viewBox="0 0 18 18"><ellipse class="num" cx="9" cy="9" rx="8" ry="5.5" transform="rotate(-30 9 9)"/><text class="num-text" x="5" y="11.5">05</text></svg><div class="text"><div class="name">Greek Salad</div><div class="desc">cos lettuce, tomato, onion, cucumber, olives, feta cheese &amp; dressing</div></div><div class="prices"><b class="p"><sup>$</sup>14.5</b></div></div>
      <div class="item"><svg class="icon" viewBox="0 0 18 18"><ellipse class="num" cx="9" cy="9" rx="8" ry="5.5" transform="rotate(-30 9 9)"/><text class="num-text" x="5" y="11.5">05</text></svg><div class="text"><div class="name">Grilled Chicken Salad</div><div class="desc">Seasoned chicken, mixed leaves, cherry tomato, Spanish onion, cucumber with garlic infused olive oil</div></div><div class="prices"><b class="p"><sup>$</sup>15.5</b></div></div>
      <div class="item"><svg class="icon" viewBox="0 0 18 18"><ellipse class="num" cx="9" cy="9" rx="8" ry="5.5" transform="rotate(-30 9 9)"/><text class="num-text" x="5" y="11.5">05</text></svg><div class="text"><div class="name">Chicken Ceasar Salad</div><div class="desc">Chicken, cos lettuce, croutons, shaved parmesan, anchovies, egg, bacon served with ceaser dressing</div></div><div class="prices"><b class="p"><sup>$</sup>15.5</b></div></div>
    </div>
  </div>
  <div class="band bottom"></div>
</section>

<!-- Outside spread -->
<section class="spread outside">
  <div class="band top"></div>
  <div class="panels">
    <div class="panel pasta" style="flex:1">
      <h2 class="ribbon">Pasta</h2>
      <p class="sub">Spaghetti, Penne, Gnocchi, Fettucine, Linguine</p>
      <div class="item"><svg class="icon" viewBox="0 0 18 18"><path class="num" d="M2 8h14a7 7 0 0 1-14 0z"/><text class="num-text" x="5" y="6">01</text></svg><div class="text"><div class="name">Bolognese</div><div class="desc">traditional Italian meat sauce</div></div><div class="prices"><b class="p"><sup>$</sup>14</b></div></div>
      <div class="item"><svg class="icon" viewBox="0 0 18 18"><path class="num" d="M2 8h14a7 7 0 0 1-14 0z"/><text class="num-text" x="5" y="6">02</text></svg><div class="text"><div class="name">Carbonara</div><div class="desc">onion, bacon, egg in creamy parmesan cheese sauce</div></div><div class="prices"><b class="p"><sup>$</sup>14</b></div></div>
      <div class="item"><svg class="icon" viewBox="0 0 18 18"><path class="num" d="M2 8h14a7 7 0 0 1-14 0z"/><text class="num-text" x="5" y="6">03</text></svg><div class="text"><div class="name">Napolitana</div><div class="desc">traditional Italian Napoli sauce</div></div><div class="prices"><b class="p"><sup>$</sup>13.5</b></div></div>
      <div class="item"><svg class="icon" viewBox="0 0 18 18"><path class="num" d="M2 8h14a7 7 0 0 1-14 0z"/><text class="num-text" x="5" y="6">04</text></svg><div class="text"><div class="name">Amatriciana</div><div class="desc">bacon, onion, olives, capsicum, fresh chili cooked in Napoli sauce</div></div><div class="prices"><b class="p"><sup>$</sup>15</b></div></div>
      <div class="item"><svg class="icon" viewBox="0 0 18 18"><path class="num" d="M2 8h14a7 7 0 0 1-14 0z"/><text class="num-text" x="5" y="6">05</text></svg><div class="text"><div class="name">Marinara</div><div class="desc">mussels, prawns, calamari, scallops cooked in Napoli sauce</div></div><div class="prices"><b class="p"><sup>$</sup>15</b></div></div>
      <div class="item"><svg class="icon" viewBox="0 0 18 18"><path class="num" d="M2 8h14a7 7 0 0 1-14 0z"/><text class="num-text" x="5" y="6">06</text></svg><div class="text"><div class="name">Risotto Polo</div><div class="desc">chicken, mushroom, onion, cooked in a cream sauce</div></div><div class="prices"><b class="p"><sup>$</sup>16.5</b></div></div>
      <div class="item"><svg class="icon" viewBox="0 0 18 18"><path class="num" d="M2 8h14a7 7 0 0 1-14 0z"/><text class="num-text" x="5" y="6">07</text></svg><div class="text"><div class="name">Lasagna</div><div class="desc">Homemade Lasagna</div></div><div class="prices"><b class="p"><sup>$</sup>15</b></div></div>
      <div class="item"><svg class="icon" viewBox="0 0 18 18"><path class="num" d="M2 8h14a7 7 0 0 1-14 0z"/><text class="num-text" x="5" y="6">08</text></svg><div class="text"><div class="name">Pasta Your Way</div><div class="desc">choose any three ingredients with cream or Napoli sauce</div></div><div class="prices"><b class="p"><sup>$</sup>14.5</b></div></div>
      <h2 class="ribbon" style="margin-top:6px">Combo Deals</h2>
      <div class="item"><svg class="icon" viewBox="0 0 18 18"><rect class="num" x="1.5" y="5" width="15" height="10"/><text class="num-text" x="5" y="13">01</text></svg><div class="text"><div class="name">Any 2 Family pizzas, garlic bread and 1.25l soft drink</div></div><div class="prices"><b class="p"><sup>$</sup>41</b></div></div>
      <div class="item"><svg class="icon" viewBox="0 0 18 18"><rect class="num" x="1.5" y="5" width="15" height="10"/><text class="num-text" x="5" y="13">02</text></svg><div class="text"><div class="name">1 Large pizza, 1 pasta, garlic bread and 1.25l soft drink</div></div><div class="prices"><b class="p"><sup>$</sup>38</b></div></div>
      <div class="item"><svg class="icon" viewBox="0 0 18 18"><rect class="num" x="1.5" y="5" width="15" height="10"/><text class="num-text" x="5" y="13">03</text></svg><div class="text"><div class="name">2 Large pizzas, 1 garlic bread and 1.25l soft drink</div></div><div class="prices"><b class="p"><sup>$</sup>36</b></div></div>
    </div>

    <div class="panel simple" style="flex:1">
      <h2 class="ribbon">Kids Menu</h2>
      <div class="kids"><span class="price"><sup>$</sup>9.5</span><ul><li>Pasta Bolognese</li><li>Pasta Napoli</li><li>Chicken Nuggets &amp; Chips</li><li>Cheeseburger &amp; Chips</li></ul></div>
      <h2 class="ribbon">Sides</h2>
      <div class="item"><div class="text"><div class="name">{01} Garlic Bread</div></div><div class="prices"><b class="p"><sup>$</sup>4.5</b></div></div>
      <div class="item"><div class="text"><div class="name">{02} Chips</div></div><div class="prices"><b class="p"><sup>$</sup>7.5</b></div></div>
      <div class="item"><div class="text"><div class="name">{03} Garden Salad</div></div><div class="prices"><b class="p"><sup>$</sup>5</b></div></div>
      <h2 class="ribbon" style="margin-top:4px">Desserts</h2>
      <div class="item"><div class="text"><div class="name">Gelati 500mls varieties</div></div><div class="prices"><b class="p"><sup>$</sup>6.5</b></div></div>
      <div class="item"><div class="text"><div class="name">Baci</div></div><div class="prices"><b class="p"><sup>$</sup>6</b></div></div>
      <div class="item"><div class="text"><div class="name">Tartufo</div></div><div class="prices"><b class="p"><sup>$</sup>6</b></div></div>
      <div class="item"><div class="text"><div class="name">Chocolate Mousse</div></div><div class="prices"><b class="p"><sup>$</sup>6</b></div></div>
      <h2 class="ribbon" style="margin-top:4px">Drinks</h2>
      <div class="item"><div class="text"><div class="name">Soft drinks 375ml</div></div><div class="prices"><b class="p"><sup>$</sup>2.5</b></div></div>
      <div class="item"><div class="text"><div class="name">Soft drinks 1.25l</div></div><div class="prices"><b class="p"><sup>$</sup>4.5</b></div></div>
      <div class="item"><div class="text"><div class="name">Water 600ml</div></div><div class="prices"><b class="p"><sup>$</sup>2.5</b></div></div>
    </div>

    <div class="panel cover" style="flex:1">
      <div class="cover-art" role="img" aria-label="Line drawings of pizza, vegetables, cheese, herbs and seafood"></div>
      <div class="brand">
        <span class="dot"></span>
        <div class="brand-name">CORVELLO<br>PIZZERIA</div>
      </div>
      <p class="contact">Address : 27 Larkfield Rd,<br>Larkfield 3051<br>Tel:<br>Website/ Online ordering:</p>
    </div>
  </div>
  <div class="band bottom"></div>
</section>

</body>
</html>
```